New Business Card Design Project

I need a design for business cards, i am an electrical business called "Vantor Electrical and Communications" i need the cards to be double sided with the company logo on the back (attached) the front needs to say my company name, web site, email address, telephone number, and ABN number and electrical license number. I am open to different arrangements of the information but would like the background to be incorporating something electrical or something that looks smart. open to all additional ideas also.

The company colours are orange and grey see logo attached.

Business Name: Vantor Electrical and Communications
Website: vantorelectricalandcomms.example.au
Email: dean@vantorelectricalandcomms.example.au
Telephone(mobile): 0481290736
ABN: 71829304516
Lic No: 483027D

Target Market(s)

Business entities, Project Managers, Accounts, Clients

Industry/Entity Type

Electrician

Contact Information for Business Card

I need a design for business cards, i am an electrical business called "Vantor Electrical and Communications" i need the cards to be double sided with the company logo on the back (attached) the front needs to say my company name

Font styles to use
Serif
Sans Serif

Colors
f37122
5c5c5c

Requirements
Must have
• Must have the Logo on the back open to different ways of it being on the back but had in mind to keep it central but again open to other options
Nice to have
• A real modern cool background that is eye catching yet contemporary
Should not have
• No backgrounds of a light bulb or plug or anything like that

```html
<!DOCTYPE html>
<html lang="en">
<head>
<meta charset="utf-8">
<title>Vantor Electrical and Communications – Business Cards</title>
<link href="https://fonts.googleapis.com/css2?family=Arimo:wght@400;700&display=swap" rel="stylesheet">
<style>
  :root {
    --page: #e6e6e4;
    --card-dark: #474747;
    --card-mid: #5c5c5c;
    --card-light: #6a6a6a;
    --orange: #f5a21b;
    --orange-deep: #f37122;
    --text-light: #f2f2f2;
    --text-soft: #d9d9d9;
  }
  * { box-sizing: border-box; margin: 0; padding: 0; }
  html, body {
    width: 1200px; height: 950px; overflow: hidden;
    background: var(--page);
    font-family: "Arimo", Arial, sans-serif;
  }
  .canvas {
    position: relative; width: 1200px; height: 950px;
  }
  .card {
    position: absolute; left: 220px; width: 760px; height: 434px;
    border-radius: 4px;
    background: linear-gradient(115deg, var(--card-dark) 0%, var(--card-mid) 55%, var(--card-light) 100%);
    box-shadow: 0 6px 18px rgba(0,0,0,.25);
    color: var(--text-light);
    overflow: hidden;
  }
  .card--back { top: 26px; }
  .card--front { top: 490px; }

  /* back */
  .brand {
    position: absolute; left: 0; right: 0; top: 150px;
    text-align: center;
  }
  .brand__name {
    font-weight: 700; font-size: 52px; letter-spacing: 4px;
    color: var(--text-light); text-transform: uppercase;
  }
  .brand__sub {
    margin-top: 10px;
    font-weight: 700; font-size: 17px; letter-spacing: 2px;
    color: var(--text-light); text-transform: uppercase;
  }
  .back-web {
    position: absolute; left: 0; right: 0; bottom: 40px;
    text-align: center; font-size: 18px; color: var(--text-soft);
  }

  /* front */
  .person {
    position: absolute; left: 380px; top: 48px;
  }
  .person__name {
    font-weight: 700; font-size: 24px; color: var(--orange); letter-spacing: .5px;
  }
  .person__role {
    font-size: 18px; color: var(--text-light); margin-top: 2px;
  }
  .cord-art {
    position: absolute; left: 110px; top: 108px; width: 560px; height: 150px;
    border-radius: 6px;
    background: linear-gradient(90deg, rgba(245,162,27,.55), rgba(245,162,27,.15));
  }
  .contact {
    position: absolute; left: 70px; top: 300px;
    font-size: 19px; line-height: 27px; color: var(--text-light);
  }
  .contact__row { display: flex; align-items: center; white-space: nowrap; }
  .contact__row--abn { padding-left: 92px; }
  .contact__row--web { padding-left: 78px; }
  .contact__gap { width: 14px; }
  .icon { width: 16px; height: 16px; margin-right: 7px; flex: none; }
</style>
</head>
<body>
<div class="canvas">

  <section class="card card--back" aria-label="Card back">
    <div class="brand">
      <div class="brand__name">Vantor</div>
      <div class="brand__sub">Electrical &amp; Communications</div>
    </div>
    <div class="back-web">vantorelectricalandcomms.example.au</div>
  </section>

  <section class="card card--front" aria-label="Card front">
    <div class="cord-art" role="img" aria-label="Orange plug with a wavy cord decoration"></div>

    <div class="person">
      <div class="person__name">DEAN MARLOW</div>
      <div class="person__role">PRESIDENT</div>
    </div>

    <div class="contact">
      <div class="contact__row contact__row--abn">ABN: 71829304516 &nbsp;|&nbsp; Lic No: 483027D</div>
      <div class="contact__row">
        <svg class="icon" viewBox="0 0 16 16" aria-hidden="true">
          <rect x="4" y="1" width="8" height="14" rx="1.5" fill="none" stroke="var(--orange)" stroke-width="1.8"/>
          <circle cx="8" cy="12.3" r="1" fill="var(--orange)"/>
        </svg>
        0481290736
        <span class="contact__gap"></span>
        <svg class="icon" viewBox="0 0 16 16" aria-hidden="true">
          <rect x="1" y="3" width="14" height="10" rx="1" fill="var(--orange)"/>
          <path d="M1.5 3.8 8 9 14.5 3.8" fill="none" stroke="var(--card-dark)" stroke-width="1.3"/>
        </svg>
        dean@vantorelectricalandcomms.example.au
      </div>
      <div class="contact__row contact__row--web">
        <svg class="icon" viewBox="0 0 16 16" aria-hidden="true">
          <circle cx="8" cy="8" r="7" fill="var(--orange)"/>
          <path d="M1 8h14M8 1c-3 3-3 11 0 14M8 1c3 3 3 11 0 14" fill="none" stroke="var(--card-dark)" stroke-width="1"/>
        </svg>
        vantorelectricalandcomms.example.au
      </div>
    </div>
  </section>

</div>
</body>
</html>
```